Consulting Company needs business card design

We need a business card design for a new consulting and business solutions company based in Bermuda called Corvale Partners Limited. Looking for a double sided business card with one side only including the company logo thats attached and the other including contact information. Logo contains blue and turquoise colors and is fine to be on both sides of the card.
Contact Information for Business Card
Corvale Partners Limited
P.O. Box HM318
Devonshire DV BX
Bermuda
Name: Marcus Pellegrin
Position: Director
Telephone: 1 441 733 4906
Email: mpellegrin@corvale.example
Website: www.corvale.example

```html
<!DOCTYPE html>
<html lang="en">
<head>
<meta charset="utf-8">
<title>Corvale Partners Limited – Business Card</title>
<link href="https://fonts.googleapis.com/css2?family=Arimo:wght@400;700&display=swap" rel="stylesheet">
<style>
  :root {
    --stage: #1a1c21;
    --card: #0b1019;
    --card-edge: #151b26;
    --blue: #1e9fe0;
    --teal: #17b3ad;
    --faint: #141b26;
    --rule: #138f93;
  }
  * { margin: 0; padding: 0; box-sizing: border-box; }
  html, body { width: 1200px; height: 800px; overflow: hidden; }
  body {
    background: var(--stage);
    font-family: "Arimo", Arial, sans-serif;
    position: relative;
  }
  .card {
    position: absolute;
    width: 540px;
    height: 309px;
    background: var(--card);
    border: 1px solid var(--card-edge);
    box-shadow: 0 18px 40px rgba(0,0,0,0.55);
    overflow: hidden;
  }
  .card--front { left: 70px; top: 80px; }
  .card--back { left: 590px; top: 410px; }

  .brand {
    position: absolute;
    display: flex;
    align-items: center;
    gap: 12px;
  }
  .brand__dot {
    width: 30px; height: 30px;
    border-radius: 50%;
    background: var(--blue);
    flex: none;
  }
  .brand__name {
    color: var(--blue);
    font-weight: 700;
    font-size: 24px;
    letter-spacing: 1px;
    text-transform: uppercase;
    line-height: 1;
  }
  .card--front .brand { left: 50%; top: 50%; transform: translate(-50%, -50%); }
  .card--back .brand { left: 70px; top: 112px; }
  .card--back .brand__name { font-size: 20px; }
  .card--back .brand__dot { width: 26px; height: 26px; }

  .backdrop-disc {
    position: absolute;
    right: 50px; top: -30px;
    width: 210px; height: 210px;
    border-radius: 50%;
    background: var(--faint);
  }

  .divider {
    position: absolute;
    left: 40px; right: 40px; top: 206px;
    height: 1px;
    background: var(--rule);
  }

  .address {
    position: absolute;
    right: 48px; top: 150px;
    text-align: right;
    color: var(--blue);
    font-size: 11.5px;
    line-height: 1.35;
  }

  .person {
    position: absolute;
    left: 44px; top: 172px;
    color: var(--blue);
  }
  .person__name { font-weight: 700; font-size: 15px; line-height: 1.1; }
  .person__role { font-size: 12px; line-height: 1.2; }

  .contacts {
    position: absolute;
    left: 44px; top: 216px;
    list-style: none;
    color: var(--blue);
    font-size: 11.5px;
  }
  .contacts li { display: flex; align-items: center; gap: 8px; height: 19px; }
  .contacts svg { width: 14px; height: 14px; flex: none; }
</style>
</head>
<body>

  <section class="card card--front" aria-label="Business card front">
    <div class="brand">
      <span class="brand__dot"></span>
      <span class="brand__name">Corvale Partners Limited</span>
    </div>
  </section>

  <section class="card card--back" aria-label="Business card back">
    <div class="backdrop-disc" role="img" aria-label="Faint large brand disc"></div>

    <div class="brand">
      <span class="brand__dot"></span>
      <span class="brand__name">Corvale Partners Limited</span>
    </div>

    <address class="address">
      P.O. Box HM318<br>
      Devonshire DV BX<br>
      Bermuda
    </address>

    <div class="person">
      <div class="person__name">Marcus Pellegrin</div>
      <div class="person__role">Director</div>
    </div>

    <div class="divider"></div>

    <ul class="contacts">
      <li>
        <svg viewBox="0 0 14 14" aria-hidden="true"><circle cx="7" cy="7" r="6.3" fill="none" stroke="#17b3ad"/><path d="M4.6 3.8l1.3 1.4-.7.9a5 5 0 0 0 2.7 2.7l.9-.7 1.4 1.3-.8 1c-2.8-.3-5.5-3-5.8-5.8z" fill="#17b3ad"/></svg>
        1 441 733 4906
      </li>
      <li>
        <svg viewBox="0 0 14 14" aria-hidden="true"><circle cx="7" cy="7" r="6.3" fill="none" stroke="#17b3ad"/><rect x="3.8" y="4.8" width="6.4" height="4.4" fill="#17b3ad"/><path d="M3.8 4.8L7 7.4l3.2-2.6" fill="none" stroke="#0b1019" stroke-width=".8"/></svg>
        mpellegrin@corvale.example
      </li>
      <li>
        <svg viewBox="0 0 14 14" aria-hidden="true"><circle cx="7" cy="7" r="6.3" fill="none" stroke="#17b3ad"/><circle cx="7" cy="7" r="3.4" fill="none" stroke="#17b3ad" stroke-width=".8"/><path d="M3.6 7h6.8M7 3.6v6.8" stroke="#17b3ad" stroke-width=".8"/><ellipse cx="7" cy="7" rx="1.5" ry="3.4" fill="none" stroke="#17b3ad" stroke-width=".8"/></svg>
        www.corvale.example
      </li>
    </ul>
  </section>

</body>
</html>
```